Need a logo/cover design for my book Golden Handshake Hours: How We Turned Coffee Chats Into Fortunes With Friends Worth Keeping

Over the years I've worked in chambers of commerce and at high-profile country clubs and have had access to very successful people and the companies they work for or launch. Through meeting people, learning from them, applying what I've learned, and by connecting with them as resources and lead sources for business, I've been able to generate over $2M in the past few years. I'm sharing the roadmap I followed to create the connections and make the sales.
Updates

Combination of slow feedback on my part by not understanding the process, similar designs, and many who withdrew immediately after my first response.

Target Market(s)

Entrepreneurs and business people, specifically business owners and those in sales and marketing roles.

Industry/Entity Type

Small Business

Font styles to use
Sans Serif

Colors

Designer to choose colors to be used in the design.

Requirements
Must have
• Original graphic design. Something that looks like I paid a professional to have it done.
Nice to have
• Perhaps my picture? Not really sure
Should not have
• I'd like to avoid a look that I could have created myself using clip art and special fonts.

```html
<!DOCTYPE html>
<html lang="en">
<head>
<meta charset="utf-8">
<title>Golden Handshake Hours – Book Cover Spread</title>
<link rel="stylesheet" href="https://fonts.googleapis.com/css2?family=Bebas+Neue&family=Montserrat:wght@300;400;500;600&display=swap">
<style>
  :root {
    --page-bg: #ffffff;
    --back-navy: #1d1640;
    --front-top: #2a3782;
    --front-glow: #2c6cb8;
    --front-bottom: #101230;
    --title-orange: #f9b042;
    --title-green: #8dc63f;
    --subtitle-yellow: #f7d54e;
    --text-light: #ffffff;
    --bio-band: #e6d9d6;
    --bio-text: #2a2540;
    --photo-tone: #8a6a5c;
    --isbn-box: #ffffff;
  }
  * { box-sizing: border-box; margin: 0; padding: 0; }
  html, body {
    width: 1200px; height: 1200px; overflow: hidden;
    background: var(--page-bg);
  }
  .cover-spread {
    position: absolute; left: 81px; top: 207px;
    width: 1036px; height: 782px;
    display: flex;
  }
  /* Back cover */
  .back-cover {
    position: relative; width: 530px; height: 100%;
    background: var(--back-navy);
    font-family: "Montserrat", sans-serif;
  }
  .back-blurb {
    position: absolute; left: 49px; top: 52px; width: 410px;
    color: var(--text-light);
    font-size: 12.6px; font-weight: 300; line-height: 19.2px;
    text-align: justify;
  }
  .back-blurb p + p { margin-top: 19px; }
  .author-bio {
    position: absolute; left: 0; top: 523px; width: 506px; height: 109px;
    background: var(--bio-band);
  }
  .author-photo {
    position: absolute; left: 38px; top: 0; width: 124px; height: 109px;
    background: linear-gradient(135deg, #9a5a44 0%, var(--photo-tone) 45%, #6f8296 100%);
  }
  .author-bio-text {
    position: absolute; left: 173px; top: 3px; width: 290px;
    color: var(--bio-text);
    font-size: 10.6px; line-height: 15.4px; font-weight: 400;
  }
  .isbn-box {
    position: absolute; left: 276px; top: 648px; width: 182px; height: 101px;
    background: var(--isbn-box);
  }
  .spine-title {
    position: absolute; left: 507px; top: 298px;
    writing-mode: vertical-rl;
    font-family: "Bebas Neue", sans-serif;
    font-size: 16px; letter-spacing: 0.2px;
    color: var(--title-orange);
  }
  /* Front cover */
  .front-cover {
    position: relative; width: 506px; height: 100%;
    overflow: hidden;
    text-align: center;
  }
  .front-backdrop {
    position: absolute; inset: 0;
    background:
      radial-gradient(ellipse 70% 35% at 55% 48%, rgba(60,130,210,0.75) 0%, rgba(44,108,184,0.25) 55%, transparent 80%),
      linear-gradient(180deg, var(--front-top) 0%, #22458f 35%, #1a2f66 62%, var(--front-bottom) 100%);
  }
  .front-content { position: relative; }
  .book-title {
    font-family: "Bebas Neue", sans-serif;
    font-weight: 400;
    line-height: 0.9;
    padding-top: 52px;
  }
  .book-title span { display: block; }
  .title-golden { color: var(--title-orange); font-size: 108px; }
  .title-handshake { color: var(--title-green); font-size: 112px; }
  .title-hours { color: var(--title-orange); font-size: 108px; }
  .book-subtitle {
    margin-top: 42px;
    font-family: "Montserrat", sans-serif;
    font-weight: 300; font-size: 26px; line-height: 40px;
    color: var(--text-light);
  }
  .book-subtitle strong {
    display: block; font-weight: 600; color: var(--subtitle-yellow);
  }
  .author-name {
    position: absolute; left: 0; right: 0; top: 716px;
    font-family: "Montserrat", sans-serif;
    font-weight: 500; font-size: 23px; letter-spacing: 1px;
    color: var(--text-light);
  }
</style>
</head>
<body>
  <main class="cover-spread">
    <section class="back-cover">
      <div class="back-blurb">
        <p>Lorem ipsum dolor sit amet, consectetuer adipiscing elit, sed diam nonummy nibh euismod tincidunt ut laoreet dolore magna aliquam erat volutpat. Ut wisi enim ad minim veniam, quis nostrud exerci tation ullamcorper suscipit lobortis nisl ut aliquip ex ea commodo consequat. Duis autem vel eum iriure dolor in hendrerit in vulputate velit esse molestie consequat, vel illum dolore eu feugiat nulla facilisis at vero eros et accumsan et iusto odio dignissim qui blandit praesent luptatum zzril delenit augue duis dolore te feugait nulla facilisi.</p>
        <p>Lorem ipsum dolor sit amet, cons ectetuer adipiscing elit, sed diam nonummy nibh euismod tincidunt ut laoreet dolore magna aliquam erat volutpat. Ut wisi enim ad minim veniam, quis nostrud exerci tation ullamcorper suscipit lobortis nisl ut aliquip ex ea commodo consequat.</p>
        <p>Lorem ipsum dolor sit amet, consectetuer adipiscing elit, sed diam nonummy nibh euismod tincidunt ut laoreet dolore magna aliquam erat volutpat. Ut wisi enim ad minim veniam, quis nostrud exerci tation ullamcorper suscipit lobortis nisl ut aliquip ex ea commodo consequat. Duis autem vel eum iriure dolor in hendrerit in vulputate velit esse molestie</p>
      </div>
      <div class="author-bio">
        <div class="author-photo" role="img" aria-label="Author portrait photo in front of a brick wall"></div>
        <p class="author-bio-text">Lorem ipsum dolor sit amet, consectetuer adipiscing elit, sed diam nonummy nibh euismod tincidunt ut laoreet dolore magna aliquam erat volutpat. Ut wisi enim ad minim veniam, quis nostrud exerci tation ullamcorper suscipit lobortis nisl ut aliquip ex ea commodo consequat. Duis</p>
      </div>
      <div class="isbn-box"></div>
      <div class="spine-title">GOLDENHANDSHAKEHOURS</div>
    </section>
    <section class="front-cover">
      <div class="front-backdrop" role="img" aria-label="Blurred photo of an audience watching a speaker on a blue-lit stage"></div>
      <div class="front-content">
        <h1 class="book-title">
          <span class="title-golden">Golden</span>
          <span class="title-handshake">Handshake</span>
          <span class="title-hours">Hours</span>
        </h1>
        <p class="book-subtitle">
          How We Turned
          <strong>Coffee Chats Into Fortunes</strong>
          With Friends Worth Keeping
        </p>
      </div>
      <p class="author-name">AUTHOR NAME</p>
    </section>
  </main>
</body>
</html>
```